Webpage needed for a new legal recruitment/headhunting companyi

I would like a professional and sharp looking website to showcase a new legal headhunting/recruitment company called Ridgel. The logo for the company is attached.

I like the following websites:
http://www.brimvaleadvisory.co.uk/
(For the general style and layout- although photographs of the team will be difficult as we don't have one yet!;-))

http://qomd.co.uk/
I like the style of the photographs etc on this one.

NB the pictures attached below are for information only- I don't think I would be able to use any of them...

Hope you can help!
Many thanks

```html
<!DOCTYPE html>
<html lang="en">
<head>
<meta charset="utf-8">
<title>Ridgel — Legal Recruitment</title>
<link rel="stylesheet" href="https://fonts.googleapis.com/css2?family=Noto+Serif:ital@1&family=Open+Sans:wght@300;400;600;700&display=swap">
<style>
  :root {
    --purple-deep: #4a2b6a;
    --purple-nav: #8660ad;
    --purple-nav-edge: #6a4590;
    --purple-active: #3e2458;
    --grey-text: #9ea1a8;
    --grey-dark: #6e7076;
    --grey-tile: #c8c8c8;
    --line: #d9d9dd;
    --white: #ffffff;
  }
  * { box-sizing: border-box; margin: 0; padding: 0; }
  html, body { width: 1200px; height: 945px; overflow: hidden; background: var(--white); }
  body { position: relative; font-family: "Open Sans", Arial, sans-serif; color: var(--purple-deep); }

  .utility-bar { position: absolute; top: 0; left: 0; width: 1200px; height: 28px;
    border-top: 3px solid var(--purple-deep); border-bottom: 1px solid #cfcfd4; }
  .utility-links { position: absolute; top: 7px; display: flex; font-size: 11px; color: var(--purple-deep); }
  .utility-links span { padding: 0 11px; border-left: 1px dotted #999; line-height: 12px; }
  .utility-links span:first-child { border-left: none; padding-left: 0; }
  .utility-links.left { left: 120px; }
  .utility-links.right { left: 807px; }
  .social { position: absolute; top: 9px; left: 1008px; display: flex; gap: 14px; }
  .social i { width: 12px; height: 12px; border-radius: 50%; background: var(--purple-deep); display: block; }

  .brand { position: absolute; top: 48px; left: 488px; width: 240px; }
  .brand-row { display: flex; align-items: center; gap: 10px; }
  .brand-mark { width: 22px; height: 22px; border-radius: 50%; background: var(--purple-deep); }
  .brand-name { font-size: 50px; font-weight: 400; letter-spacing: 1px; line-height: 56px; color: var(--purple-deep); }
  .brand-tag { position: absolute; left: 121px; top: 56px; font-size: 13px; color: #8a8a90; white-space: nowrap; }

  .main-nav { position: absolute; top: 148px; left: 0; width: 1200px; height: 56px;
    background: var(--purple-nav); border-top: 2px solid var(--purple-nav-edge); border-bottom: 3px solid var(--purple-nav-edge);
    box-shadow: 0 6px 10px rgba(0,0,0,.08); }
  .main-nav a { position: absolute; top: 0; height: 51px; line-height: 57px; font-size: 15px; color: var(--white); text-decoration: none; }
  .main-nav a.current { color: var(--purple-active); border-top: 3px solid var(--purple-active); top: -4px; line-height: 58px; text-align: center; }
  .main-nav .sep { position: absolute; top: 17px; width: 1px; height: 34px; background: rgba(255,255,255,.35); }

  .hero { position: absolute; top: 206px; left: 121px; width: 958px; height: 281px; background: #fafafa;
    box-shadow: 0 2px 8px rgba(0,0,0,.12); }
  .hero-photo { position: absolute; left: 0; top: 0; width: 823px; height: 281px;
    background: linear-gradient(90deg, #9a9a9a 0%, #6d6d6d 25%, #cfcfcf 45%, #e4e4e4 70%, #f6f6f6 100%); }
  .hero-headline { position: absolute; left: 646px; top: 20px; width: 240px; text-align: center; color: var(--purple-deep); }
  .hero-year { font-size: 104px; font-weight: 300; line-height: 106px; letter-spacing: 2px; }
  .hero-record { font-size: 28px; font-weight: 400; line-height: 30px; }
  .hero-for { display: flex; align-items: center; gap: 6px; margin: 6px 0 0 6px; font-family: "Noto Serif", Georgia, serif; font-style: italic; font-size: 17px; }
  .hero-for::before, .hero-for::after { content: ""; flex: 1; height: 1px; background: var(--purple-deep); }
  .hero-business { font-size: 50px; font-weight: 700; line-height: 56px; margin-left: -4px; }

  .tweet-bar { position: absolute; top: 489px; left: 121px; width: 934px; height: 34px; border-bottom: 1px solid var(--line); }
  .tweet-label { position: absolute; left: 0; top: 0; width: 99px; height: 33px; background: var(--purple-deep); color: var(--white);
    font-size: 15px; line-height: 33px; padding-left: 34px; }
  .tweet-label::before { content: ""; position: absolute; left: 11px; top: 11px; width: 12px; height: 11px; background: var(--white); }
  .tweet-text { position: absolute; left: 116px; top: 8px; font-family: "Noto Serif", Georgia, serif; font-style: italic; font-size: 14px; color: var(--grey-dark); white-space: nowrap; }
  .tweet-text b { color: var(--purple-deep); font-weight: 400; }
  .tweet-arrows { position: absolute; left: 883px; top: 7px; display: flex; gap: 7px; }
  .tweet-arrows svg { display: block; }

  .welcome { position: absolute; top: 548px; left: 120px; width: 640px; }
  .welcome h1 { font-size: 30px; font-weight: 300; line-height: 38px; color: var(--purple-deep); margin-bottom: 10px; }
  .welcome p { font-size: 17px; line-height: 21.5px; color: var(--grey-text); margin-bottom: 21.5px; }

  .side-links { position: absolute; top: 548px; left: 776px; width: 304px; }
  .side-links a { position: absolute; left: 0; width: 304px; height: 54px; line-height: 54px; padding-left: 20px;
    font-size: 20px; font-weight: 700; color: var(--white); text-decoration: none; }
  .side-links .dark { background: var(--purple-deep); }
  .side-links .light { background: var(--grey-tile); }

  .site-footer { position: absolute; top: 892px; left: 70px; width: 1060px; height: 48px;
    border-top: 1px solid; border-image: linear-gradient(90deg, transparent, #d5d5d8 15%, #d5d5d8 85%, transparent) 1; }
  .footer-mark { position: absolute; left: 57px; top: 12px; width: 24px; height: 24px; border-radius: 50%; background: var(--purple-deep); }
  .footer-copy { position: absolute; left: 102px; top: 18px; font-size: 13px; color: var(--grey-dark); }
  .footer-rule { position: absolute; left: 0; top: 940px; width: 1200px; height: 5px; background: var(--purple-deep); }
</style>
</head>
<body>
  <header class="utility-bar">
    <nav class="utility-links left"><span>REPORT</span><span>SHORT CODE</span><span>PURCHASE</span></nav>
    <nav class="utility-links right"><span>FEED BACK</span><span>RSS</span><span>FEED BACK</span></nav>
    <div class="social"><i></i><i></i><i></i></div>
  </header>

  <div class="brand">
    <div class="brand-row"><span class="brand-mark"></span><span class="brand-name">RIDGEL</span></div>
    <span class="brand-tag">Legal Recruitment</span>
  </div>

  <nav class="main-nav">
    <a class="current" style="left:139px;width:106px">HOME</a>
    <span class="sep" style="left:250px"></span>
    <a style="left:279px">CANDIDATES</a>
    <span class="sep" style="left:400px"></span>
    <a style="left:431px">YOUR TEAM</a>
    <span class="sep" style="left:545px"></span>
    <a style="left:578px">CLIENTS</a>
    <span class="sep" style="left:671px"></span>
    <a style="left:699px">YOUR TEAM</a>
    <span class="sep" style="left:815px"></span>
    <a style="left:849px">BLOGS</a>
  </nav>

  <section class="hero">
    <div class="hero-photo" role="img" aria-label="Black and white portrait of a smiling businessman in a suit in front of blurred office buildings"></div>
    <div class="hero-headline">
      <div class="hero-year">2013</div>
      <div class="hero-record">was a record year</div>
      <div class="hero-for">for our</div>
      <div class="hero-business">BUSINESS</div>
    </div>
  </section>

  <div class="tweet-bar">
    <div class="tweet-label">TWEET</div>
    <div class="tweet-text"><b>20 June 2009 :</b> 37 billion (US$ 625 million) annually. Group assets exceed Rupees 17 billion (US$ 280 million)</div>
    <div class="tweet-arrows">
      <svg width="21" height="21" viewBox="0 0 21 21"><circle cx="10.5" cy="10.5" r="9.5" fill="#fff" stroke="#cfcfd4"/><path d="M12 7 L8.5 10.5 L12 14" fill="none" stroke="#333" stroke-width="2"/></svg>
      <svg width="21" height="21" viewBox="0 0 21 21"><circle cx="10.5" cy="10.5" r="9.5" fill="#fff" stroke="#cfcfd4"/><path d="M9 7 L12.5 10.5 L9 14" fill="none" stroke="#333" stroke-width="2"/></svg>
    </div>
  </div>

  <main class="welcome">
    <h1>Welcome to RIDGEL</h1>
    <p>Brimvale is very clear about what it stands for. We are a firm of<br>headhunters servicing the legal sector. Our aim is to find our<br>clients the best lawyers in the market. They may not necessarily be the best<br>lawyers actively considering a move.</p>
    <p>We take our work and our clients seriously, but not ourselves.<br>We believe that you can be professional, creative, ethical, focused and suc-<br>cessful and still keep a smile on your face.</p>
    <p>That’s why our clients, our targets, our candidates and our<br>colleagues enjoy working with us. Feel free to ask them!</p>
  </main>

  <aside class="side-links">
    <a class="dark" style="top:0">Wha we are working on</a>
    <a class="light" style="top:66px;padding-left:18px">Recent Successes</a>
    <a class="dark" style="top:140px;padding-left:18px">Real Salaries</a>
    <a class="light" style="top:206px">Testimonials</a>
  </aside>

  <footer class="site-footer">
    <span class="footer-mark"></span>
    <span class="footer-copy">Copyright © 2014 Ridgel.</span>
  </footer>
  <div class="footer-rule"></div>
</body>
</html>
```